Ingenieurbüro seit 2004 sucht Design
Wir waren mit Frau Derrbach mehr als zufrieden. Vielen Dank für das exzellente corporate identity. Wir freuen uns auf zukünftige Zusammenarbeit.
Zielgruppe
Wir sind der Experte wenn es um die Planung der Gebäudeauotmation in Bauprojekten geht. Wir planen für Unternehmen oder öffentliche Bauherren.
Durch eine Produktneutrale Planung vernetzen wir Heizung, Lüftung, Klima und andere Gebäude-Technik zu einem optimalen Gesamtsystem. Hierbei steigern wir die Effizienz, Komfort und Sicherheit im Gebäude. (keine Hausautomation sondern für große Gebäude)
Wir heben uns gegenüber anderen Planungsbüros durch unsere produktneutrale Planung ab und dadurch, dass wir nur auf den Gebäudeautomationsbereich spezialisiert sind.
Gebäudeautomation ist ähnlich wie Hausautomation, jedoch wie der Name schon sagt für das große Gebäude z.B: Krankenhäuser, Stadtverwaltungen, öffentliche Gebäude, Hochschulen, Banken, Hotels, Pharmakonzerne...
Unser Kunde sind Entscheider ab ca. 45 Jahren, männlich, Architekten Ingenieure aber auch kaufmännisch geprägte Bauherren.
Aufgabenstellung
Der Name Lind und Faber sollte vorhanden bleiben, da er seit 2004 als Marke etabliert ist.
Wir haben zwei Ideen, sind aber für jede weitere Idee sehr dankbar.
1.Variante: Lind + Faber <-- Wie das berühmte Architekturbüro: Halden + Kollegen
4.Variante siehe Skizze 4 (vernetzt)
Für ein junges europäisches Unternehmen im Bereich Architektur wurde ein ästhetisches und ansprechendes Corporate Design gesucht. Schwarz und weiß stehen für ein klassisches Look &amp; Feel.

```html
<!DOCTYPE html>
<html lang="de">
<head>
<meta charset="utf-8">
<title>Lind und Faber – Corporate Design</title>
<link href="https://fonts.googleapis.com/css2?family=Questrial&family=Catamaran:wght@400;600&display=swap" rel="stylesheet">
<style>
:root{
  --blue:#2a9be0;
  --ink:#55595e;
  --text:#2f3236;
  --band:#5e5e5e;
  --paper:#ffffff;
  --ground:#f2f2f2;
  --line:#d9d9d9;
}
*{margin:0;padding:0;box-sizing:border-box}
html,body{width:699px;height:1200px;overflow:hidden}
body{position:relative;background:var(--ground);font-family:"Questrial",sans-serif;color:var(--ink)}
.stage-top{position:absolute;left:0;top:0;width:699px;height:386px;background:var(--paper)}
.stage-band{position:absolute;left:0;top:386px;width:699px;height:61px;background:var(--band)}

.wordmark{position:absolute;white-space:nowrap;font-family:"Catamaran",sans-serif;font-weight:400;color:var(--ink);line-height:1}
.wordmark .dot{display:inline-block;background:var(--blue);vertical-align:middle}
.wordmark.light{color:#fff}
.wordmark.light .dot{background:#fff}

.hero{left:0;width:699px;top:170px;text-align:center;font-size:22px}
.hero .dot{width:8px;height:8px;margin-right:8px}

.mini{font-size:8px}
.mini .dot{width:3px;height:3px;margin-right:3px}

.card{position:absolute;top:294px;width:200px;height:129px;background:var(--paper);box-shadow:0 1px 4px rgba(0,0,0,.25)}
.card .rule,.letter .rule{position:absolute;left:0;height:0;border-top:.7px dashed var(--blue)}
.card .rule{top:39px;width:161px}
.card .wordmark{right:12px;top:44px;font-size:10px}
.card .wordmark .dot{width:4px;height:4px;margin-right:4px}
.card-info{position:absolute;right:39px;text-align:right;font-size:5.2px;line-height:8.2px;color:var(--ink);white-space:nowrap}
.person{top:80px;font-size:5.6px}
.person b{font-weight:400;letter-spacing:.12em}
.contact{top:92px}
.link{color:var(--blue)}
.claim{top:71px}
.values{position:absolute;left:112px;right:39px;top:96px;list-style:none;font-size:5.4px;letter-spacing:.14em;line-height:8.2px;text-align:right}
.values li{position:relative;display:block}
.values svg{position:absolute;left:0;top:1.6px}

.letter{position:absolute;left:106px;top:476px;width:494px;height:699px;background:var(--paper);box-shadow:0 1px 5px rgba(0,0,0,.2)}
.letter .rule{top:61px;width:428px}
.letter .wordmark{right:28px;top:67px;font-size:13.5px}
.letter .wordmark .dot{width:5px;height:5px;margin-right:5px}
.fold{position:absolute;left:10px;width:7px;border-top:.5px solid var(--line)}
.sender{position:absolute;left:59px;top:115px;font-size:4.6px;color:var(--ink)}
.recipient{position:absolute;left:59px;top:134px;font-size:8px;line-height:11.7px;color:var(--text);letter-spacing:.03em}
.recipient .city{margin-top:5px}
.copy{position:absolute;left:59px;width:392px;font-family:"Catamaran",sans-serif;font-size:8.1px;line-height:11.7px;color:var(--text)}
.subject{top:234px;font-weight:600}
.salutation{top:281px}
.body{top:311px}
.body p{margin-bottom:5.6px}
.closing{top:559px}
.signature{position:absolute;left:59px;top:574px;width:108px;height:34px;background:linear-gradient(90deg,#e9eaeb,#f6f6f6)}
.signer{top:616px}
.letter-foot{position:absolute;right:67px;text-align:right;font-size:5.4px;line-height:9.4px;color:var(--ink);white-space:nowrap}
.foot-contact{top:612px}
.foot-legal{top:648px}
</style>
</head>
<body>
<div class="stage-top"></div>
<div class="stage-band"></div>

<div class="wordmark hero"><span class="dot"></span>Lind und Faber</div>

<div class="wordmark mini" style="left:42px;top:355px"><span class="dot"></span>Lind und Faber</div>
<div class="wordmark mini" style="left:148px;top:355px"><span class="dot" style="background:var(--ink)"></span>Lind und Faber</div>
<div class="wordmark mini light" style="left:95px;top:419px"><span class="dot"></span>Lind und Faber</div>

<section class="card" style="left:271px">
  <div class="rule"></div>
  <div class="wordmark"><span class="dot"></span>Lind und Faber</div>
  <div class="card-info person"><b>VORNAME NACHNAME</b> | Positionsbezeichnung</div>
  <div class="card-info contact">Talbrunnenweg 7 | 55299 Weilerbach<br>T +49 6100 482150-1 | F +49 6100 482150-9<br>info@lfplan.de | <span class="link">www.lfplan.de</span></div>
</section>

<section class="card" style="left:480px">
  <div class="rule"></div>
  <div class="wordmark"><span class="dot"></span>Lind und Faber</div>
  <div class="card-info claim">Optimale Vernetzung von Gebäude-<br>Techniksystemen für ein Plus an</div>
  <ul class="values">
    <li><svg width="5" height="5" viewBox="0 0 5 5"><path d="M2.5 0v5M0 2.5h5" stroke="#2a9be0" stroke-width=".6"/></svg>EFFIZIENZ</li>
    <li><svg width="5" height="5" viewBox="0 0 5 5"><path d="M2.5 0v5M0 2.5h5" stroke="#2a9be0" stroke-width=".6"/></svg>KOMFORT</li>
    <li><svg width="5" height="5" viewBox="0 0 5 5"><path d="M2.5 0v5M0 2.5h5" stroke="#2a9be0" stroke-width=".6"/></svg>SICHERHEIT</li>
  </ul>
</section>

<article class="letter">
  <div class="rule"></div>
  <div class="wordmark"><span class="dot"></span>Lind und Faber</div>
  <div class="fold" style="top:247px"></div>
  <div class="fold" style="top:349px"></div>
  <div class="sender">Lind und Faber | Talbrunnenweg | 55299 Weilerbach</div>
  <div class="recipient">
    Firma Mustermann<br>Frau Musterfrau<br>Musterstraße 12
    <div class="city">12345 Musterstadt</div>
  </div>
  <div class="copy subject">Betrifft: Lorem ipsdum Dolores diamus</div>
  <div class="copy salutation">Sehr geehrte Frau Musterfrau,</div>
  <div class="copy body">
    <p>Lorem ipsum dolor sit amet, consetetur sadipscing elitr, sed diam nonumy eirmod tempor invidunt ut labore et dolore magna aliquyam erat, sed diam voluptua. At vero eos et accusam et justo duo dolores<br>et ea rebum. Stet clita kasd gubergren, no sea takimata sanctus est Lorem ipsum dolor sit amet. Lorem ipsum dolor sit amet, consetetur sadipscing elitr, sed diam nonumy eirmod tempor invidunt ut labore et dolore magna aliquyam erat, sed diam voluptua. d diam voluptua. At vero eos et accusam et justo duo dolores<br>et ea rebum. Stet clita kasd gubergren.</p>
    <p>At vero eos et accusam et justo duo dolores et ea rebum. Stet clita kasd gubergren, no sea takimata sanctus est Lorem ipsum dolor sit amet. Lorem ipsum dolor sit amet, consetetur sadipscing elitr, sed diam nonumy eirmod tempor invidunt ut labore et dolore magna aliquyam erat, sed diam voluptua. At vero Stet clita kasd gubergren, no sea takimata sanctus est Lorem ipsum dolor sit amet. Duis autem vel eum iriure dolor in hendrerit in vulputate velit esse molestie consequat, vel illum dolore eu feugiat nulla facilisis at vero eros et accumsan et iusto odio dignissim qui blandit praesent luptatum zzril delenit augue duis dolore te feugait nulla facilisi. Lorem ipsum dolor sit amet.</p>
    <p>Lorem ipsum dolor sit amet, consetetur sadipscing elitr, sed diam nonumy eirmod tempor invidunt ut labore et dolore magna aliquyam erat, sed diam voluptua. At vero eos et accusam et justo duo dolores<br>et ea rebum. Stet clita kasd gubergren, no sea takimata sanctus est Lorem ipsum dolor sit amet. Lorem ipsum dolor sit amet, consetetur sadipscing elitd diam voluptua. At vero eos et accusam et justo duo dolores<br>et ea rebum. Stet clita kasd gubergren.</p>
  </div>
  <div class="copy closing">Mit freundlichen Grüßen</div>
  <div class="signature" role="img" aria-label="Handschriftliche Unterschrift"></div>
  <div class="copy signer">Vorname Nachname</div>
  <div class="letter-foot foot-contact">Talbrunnenweg 7 | 55299 Weilerbach<br>T +49 6100 482150-1 | F +49 6100 482150-9<br>info@lfplan.de | www.lfplan.de</div>
  <div class="letter-foot foot-legal">Musterbankname | IBAN DE00 000 000 000 0000000 00 | BIC XXXX DE 00XXX<br>Geschäftsführung Manuel Mustefrau<br>Amtsgericht Musterstadt HRB 000 00 | USt-IdNr. DE 000 000 000</div>
</article>
</body>
</html>
```